Bref créative
Veloran Lending Group
Mortgage Lender
Professional
Gustav Kolbe
President
318 Birchwell Avenue
Regina, SK, S2K 8P4
Ph (306) 555-0142
Cl (306) 555-0187
Fx (306) 555-0143
gustav@veloran.ca
www.veloran.ca

```html
<!DOCTYPE html>
<html lang="en">
<head>
<meta charset="utf-8">
<title>Veloran Lending Group – Business Card</title>
<link rel="stylesheet" href="https://fonts.googleapis.com/css2?family=Libre+Baskerville:wght@400;700&display=swap">
<style>
  :root {
    --page: #e6e6e6;
    --red: #d8100e;
    --red-deep: #b50a08;
    --white: #ffffff;
    --paper: #f7f7f7;
    --ink: #222222;
    --ink-soft: #444444;
    --rule: #d9d9d9;
  }
  * { margin: 0; padding: 0; box-sizing: border-box; }
  html, body { width: 1200px; height: 901px; overflow: hidden; }
  body {
    background: var(--page);
    font-family: "Libre Baskerville", "Times New Roman", serif;
    position: relative;
  }
  .card {
    position: absolute;
    left: 280px;
    width: 640px;
    height: 366px;
    box-shadow: 0 6px 18px rgba(0,0,0,0.18);
  }
  .card--back {
    top: 70px;
    background: linear-gradient(160deg, var(--red) 0%, var(--red) 55%, var(--red-deep) 100%);
    color: var(--white);
  }
  .card--front {
    top: 465px;
    background: linear-gradient(180deg, var(--white), var(--paper));
    color: var(--ink);
  }
  .brand {
    position: absolute;
    display: flex;
    align-items: center;
    gap: 10px;
    font-weight: 400;
    letter-spacing: 1px;
    text-transform: uppercase;
    white-space: nowrap;
  }
  .brand__mark { width: 14px; height: 14px; background: currentColor; }
  .card--back .brand { left: 0; right: 0; justify-content: center; top: 148px; font-size: 22px; }
  .card--back .web {
    position: absolute; left: 0; right: 0; top: 262px;
    text-align: center; font-size: 15px; letter-spacing: 7px;
    color: rgba(255,255,255,0.85);
  }
  .card--front .brand { left: 34px; top: 152px; font-size: 17px; color: var(--ink); }
  .divider {
    position: absolute; left: 352px; top: 0; bottom: 0;
    width: 1px; background: var(--rule);
  }
  .contact { position: absolute; left: 378px; top: 30px; }
  .contact__name { color: var(--red); font-size: 18px; }
  .contact__role { font-size: 12px; color: var(--ink-soft); margin-top: 4px; }
  .contact__address { font-size: 13px; line-height: 1.45; margin-top: 44px; }
  .contact__list { list-style: none; margin-top: 26px; font-size: 13px; }
  .contact__list li { display: flex; align-items: center; gap: 10px; height: 20px; }
  .contact__list svg { width: 14px; height: 14px; flex: none; }
  .accent { color: var(--red); }
</style>
</head>
<body>
  <section class="card card--back">
    <div class="brand"><span class="brand__mark"></span>Veloran Lending Group</div>
    <div class="web">WWW.VELORAN.CA</div>
  </section>

  <section class="card card--front">
    <div class="brand"><span class="brand__mark" style="background: var(--red)"></span>Veloran Lending Group</div>
    <div class="divider"></div>
    <div class="contact">
      <div class="contact__name">Gustav Kolbe</div>
      <div class="contact__role">President</div>
      <div class="contact__address">318 Birchwell Avenue<br>Regina, SK, S2K 8P4</div>
      <ul class="contact__list">
        <li>
          <svg viewBox="0 0 14 14" aria-hidden="true"><path fill="#d8100e" d="M2 5c0-2 2-3 5-3s5 1 5 3l-2 1-1-2H5L4 6zM3 7h8l1 5H2z"/></svg>
          (306) 555-0142
        </li>
        <li>
          <svg viewBox="0 0 14 14" aria-hidden="true"><rect x="3" y="1" width="8" height="4" fill="none" stroke="#d8100e"/><rect x="1" y="5" width="12" height="7" rx="1" fill="#d8100e"/></svg>
          (306) 555-0143
        </li>
        <li>
          <svg viewBox="0 0 14 14" aria-hidden="true"><rect x="4" y="1" width="6" height="12" rx="1" fill="#d8100e"/><rect x="5" y="3" width="4" height="5" fill="#fff"/></svg>
          (306) 555-0187
        </li>
        <li>
          <svg viewBox="0 0 14 14" aria-hidden="true"><rect x="1" y="3" width="12" height="8" fill="#d8100e"/><path d="M1 3l6 5 6-5" fill="none" stroke="#fff"/></svg>
          gustav@veloran.ca
        </li>
        <li>
          <svg viewBox="0 0 14 14" aria-hidden="true"><circle cx="7" cy="7" r="6" fill="#d8100e"/><path d="M1 7h12M7 1c-3 3-3 9 0 12M7 1c3 3 3 9 0 12" fill="none" stroke="#fff" stroke-width="0.8"/></svg>
          <span>www.<span class="accent">veloran</span>.ca</span>
        </li>
      </ul>
    </div>
  </section>
</body>
</html>
```